Lumorax Helpdesk overview brochure

Take the word document that is attached and turn it into a brochure. (Thinking one page, front and back.) the only existing branding/colors we have is the logo that is on the document. It may require a phone all or a bit of back and forth in text to explain some of the concepts in the attached document.

Target Market(s)

Call centers

Industry/Entity Type

It Service

Font styles to use
Sans Serif

Colors

Designer to choose colors to be used in the design.

Requirements
Must have
• A crisp professional look

```html
<!DOCTYPE html>
<html lang="en">
<head>
<meta charset="utf-8">
<title>Lumorax Helpdesk – Overview</title>
<link href="https://fonts.googleapis.com/css2?family=PT+Sans+Narrow:wght@400;700&family=PT+Sans:wght@400;700&family=Montserrat:wght@700;800&display=swap" rel="stylesheet">
<style>
  :root {
    --sky: #13a4e6;
    --sky-deep: #0d8fd0;
    --mountain: #1b6fb0;
    --panel: #c8e8fa;
    --navy: #27235c;
    --slate: #3a3f48;
    --green: #1fa34a;
    --ink: #1b1b1b;
    --white: #ffffff;
  }
  * { margin: 0; padding: 0; box-sizing: border-box; }
  html, body { width: 848px; height: 1200px; overflow: hidden; background: var(--sky); }
  .brochure {
    position: relative;
    width: 848px; height: 1200px;
    overflow: hidden;
    background: var(--sky);
    font-family: "PT Sans", Arial, sans-serif;
  }
  .backdrop { position: absolute; inset: 0; }

  .brand-panel {
    position: absolute; left: 0; top: 26px;
    width: 692px; height: 206px;
    background: var(--panel);
    border-radius: 0 26px 26px 0;
  }
  .brand {
    position: absolute; left: 28px; top: 14px;
    display: flex; align-items: center; gap: 12px;
  }
  .brand-dot {
    width: 100px; height: 100px; border-radius: 50%;
    border: 4px solid var(--slate);
  }
  .brand-name {
    font-family: "PT Sans", Arial, sans-serif;
    font-weight: 700; font-size: 36px; line-height: 36px;
    color: var(--slate); letter-spacing: 1px;
  }
  .tagline {
    position: absolute; left: 140px; top: 120px;
    font-family: "Montserrat", Arial, sans-serif; font-weight: 800;
    font-size: 31px; line-height: 33px; color: var(--navy);
    letter-spacing: -0.3px; white-space: nowrap;
  }

  .headline {
    position: absolute; left: 0; top: 0;
    font-family: "PT Sans Narrow", "Arial Narrow", sans-serif;
    font-weight: 700; color: var(--white);
  }
  .headline span { position: absolute; white-space: nowrap; letter-spacing: -0.5px; }
  .headline .line-improve { left: 68px; top: 222px; font-size: 71px; line-height: 71px; }
  .headline .line-and { left: 210px; top: 276px; font-size: 60px; line-height: 60px; font-weight: 400; color: var(--ink); }
  .headline .line-lower { left: 68px; top: 312px; font-size: 71px; line-height: 71px; }
  .headline .line-tail { left: 166px; top: 377px; font-size: 49px; line-height: 49px; color: var(--ink); }

  .photo, .icon-disc {
    position: absolute; border-radius: 50%;
    border: 7px solid var(--green);
  }
  .photo-top { left: 380px; top: 352px; width: 292px; height: 292px;
    background: radial-gradient(circle at 50% 45%, #e9c3a7 0%, #c98f6d 45%, #f1efed 80%); }
  .photo-bottom { left: 446px; top: 572px; width: 380px; height: 372px;
    background: radial-gradient(circle at 45% 45%, #c99379 0%, #6f3d2a 50%, #efefef 85%); }
  .icon-disc { left: 668px; top: 466px; width: 172px; height: 172px;
    background: var(--white); display: flex; align-items: center; justify-content: center; }

  .callout {
    position: absolute; left: 14px; top: 460px;
    width: 362px; height: 252px;
    background: var(--green); border-radius: 24px;
    padding: 16px 24px 0 14px;
    font-family: "PT Sans Narrow", "Arial Narrow", sans-serif; font-weight: 700;
    font-size: 23px; line-height: 27px; color: var(--white);
    text-align: justify;
  }

  .body-copy p {
    position: absolute; left: 13px;
    font-size: 18.5px; line-height: 20px; color: var(--ink);
    text-align: justify;
  }
  .body-copy .p1 { top: 720px; width: 426px; }
  .body-copy .p2 { top: 880px; width: 466px; }
  .body-copy .p3 { top: 960px; width: 320px; }

  .closing {
    position: absolute; left: 358px; top: 988px; width: 474px;
    font-size: 18.5px; line-height: 20px; color: var(--white);
    text-align: justify;
  }
</style>
</head>
<body>
<main class="brochure">
  <svg class="backdrop" width="848" height="1200" viewBox="0 0 848 1200" aria-hidden="true">
    <path d="M0,436 L450,436 C560,430 690,560 848,700 L848,876 C600,905 420,915 340,958 C270,1010 150,1060 0,1066 Z" fill="var(--white)"/>
    <path d="M0,1066 C150,1060 270,1010 340,958 C420,915 600,905 848,876" fill="none" stroke="var(--green)" stroke-width="6"/>
    <path d="M0,1200 L0,1120 L60,1140 L230,1108 L330,1200 Z" fill="var(--mountain)"/>
    <path d="M380,1200 L560,1150 L650,1200 Z" fill="var(--mountain)"/>
    <path d="M600,1200 L770,1125 L848,1150 L848,1200 Z" fill="var(--sky-deep)"/>
  </svg>

  <header class="brand-panel">
    <div class="brand">
      <span class="brand-dot"></span>
      <span class="brand-name">Lumorax<br>Helpdesk</span>
    </div>
    <p class="tagline">helps contact centers serve<br>new customer access channels,</p>
  </header>

  <h1 class="headline">
    <span class="line-improve">improve customer service,</span>
    <span class="line-and">and</span>
    <span class="line-lower">lower costs</span>
    <span class="line-tail">of operation</span>
  </h1>

  <div class="photo photo-top" role="img" aria-label="Photo of a smiling support agent wearing a headset"></div>
  <div class="photo photo-bottom" role="img" aria-label="Photo of a support agent with glasses wearing a headset"></div>
  <div class="icon-disc" role="img" aria-label="Headset icon">
    <svg width="90" height="80" viewBox="0 0 90 80">
      <path d="M14,48 C14,18 76,18 76,48" fill="none" stroke="#2f6db5" stroke-width="6"/>
      <rect x="6" y="42" width="16" height="26" rx="5" fill="#111"/>
      <rect x="68" y="42" width="16" height="26" rx="5" fill="#111"/>
      <path d="M74,66 C70,76 58,78 48,76" fill="none" stroke="#111" stroke-width="3"/>
      <circle cx="46" cy="76" r="4" fill="#111"/>
    </svg>
  </div>

  <section class="callout">
    The huge popularity of social media and messaging is creating customer preferences to communicate with your company using SMS text messaging, Chatterly, Teamwire, Vocia, Orbit Voice, Nestro Home, and many other new channels.
  </section>

  <section class="body-copy">
    <p class="p1">App fatigue has set in. Customers are weary of installing, updating and learning how to use mobile apps. Your customers want to communicate with you using their messaging service of choice or just talk into their smart phone, computer, Orbit Voice or similar device.</p>
    <p class="p2">Sensible automation of customer interactions on these new channels can provide better service at even lower costs of operation.</p>
    <p class="p3">According to Marlowe Research’s report, by 2020, 85% of customer interactions will be managed without a human.</p>
  </section>

  <p class="closing">Using specific techniques, Lumorax Helpdesk will help you shift some traffic from higher cost telephone calls to lower cost messaging channels. Shaping your traffic into lower cost channels has great financial benefits.</p>
</main>
</body>
</html>
```